Pet Care company needs label design for new product. Eco-friendly, amazing results helping anima...

We need a label designed for a new eco-friendly pet care product. The product is highly effective, non-medicated, 100% safe to use on all animals. The product is an aqueous solution that uses a low PH to create an environment unfavorable for the grow of bacteria and fungus. Target market is horses, dogs and cats. Most common uses will be for rain rot, hot spots, ear infections and wound care. **Bottle is green with a white sprayer. Here is the specifications for the label; Trim size: 8.375 x 4.25 (w x h), please keep all critical art at least 1/8 inch away from trim line.Bleeds: Include 1/8 inch bleeds, and keep all critical art at least 1/8 inch away from trim line.

Target Market(s)

Pet owners; horses, dogs and cats

Industry/Entity Type

Pet Care

Font styles to use
Serif

Colors

Designer to choose colors to be used in the design.

Requirements
Must have
• Images of horses, dogs, cats. Geared to the eco-friendly nature of the product. It is not "organic" but I want that kind of look.
Nice to have
• Product information uploaded.
Should not have
• I do not want the product to look cartoonish. It is a highly effective treatment for animals with skin infections. I want people to feel by looking at the product it works.

```html
<!DOCTYPE html>
<html lang="en">
<head>
<meta charset="utf-8">
<title>Mossy's Mend – Eco-Friendly Pet Care Label</title>
<link href="https://fonts.googleapis.com/css2?family=Quicksand:wght@400;500;600&family=Poppins:wght@600;700&display=swap" rel="stylesheet">
<style>
  :root {
    --page: #ffffff;
    --kraft: #c8aa7c;
    --kraft-light: #d3b98f;
    --brand-green: #2a7a4c;
    --band-green: #7c9c5a;
    --band-olive: #a2a46c;
    --band-text: #f3f1e4;
    --panel-light: #eeeeee;
    --panel-mid: #c9c9c9;
    --check-text: #7d8b58;
    --photo-warm: #b9825a;
    --photo-cream: #e2cfa8;
  }
  * { box-sizing: border-box; margin: 0; padding: 0; }
  html, body { width: 1200px; height: 1000px; overflow: hidden; background: var(--page); }
  .canvas { position: relative; width: 1200px; height: 1000px; }

  .label {
    position: absolute; left: 277px; top: 92px;
    width: 646px; height: 816px;
    background: linear-gradient(160deg, var(--kraft-light), var(--kraft) 60%);
    overflow: hidden;
  }

  .brand-mark {
    position: absolute; left: 0; right: 0; top: 70px;
    display: flex; justify-content: center;
  }
  .brand-mark svg { width: 120px; height: 120px; }

  .brand-name {
    position: absolute; left: 0; right: 0; top: 252px;
    text-align: center;
    font-family: "Quicksand", sans-serif; font-weight: 500;
    font-size: 44px; letter-spacing: 1px;
    color: var(--brand-green);
    padding-left: 60px;
  }

  .tagline-band {
    position: absolute; left: 0; right: 0; top: 311px; height: 48px;
    background: var(--band-green);
    display: flex; align-items: center; justify-content: center;
    padding-left: 50px;
    font-family: "Quicksand", sans-serif; font-weight: 500;
    font-size: 30px; color: var(--band-text);
  }

  .claim-band {
    position: absolute; left: 37px; right: 0; top: 364px; height: 83px;
    background: var(--band-olive);
    display: flex; align-items: center; justify-content: center;
    text-align: center;
    font-family: "Quicksand", sans-serif; font-weight: 500;
    font-size: 18px; line-height: 1.3; color: var(--band-text);
  }

  .feature-panel {
    position: absolute; left: 37px; right: 0; top: 447px; bottom: 0;
    background: linear-gradient(90deg, var(--panel-mid), var(--panel-light) 45%, var(--panel-mid));
  }

  .feature-list {
    position: absolute; left: 6px; top: 100px;
    list-style: none;
    font-family: "Poppins", sans-serif; font-weight: 600;
    font-size: 23px; line-height: 43px;
    color: var(--check-text);
  }
  .feature-list li { display: flex; align-items: center; gap: 4px; }
  .feature-list .tick { width: 24px; height: 24px; flex: none; }
  .feature-list .more { padding-left: 28px; }

  .volume {
    position: absolute; left: 40px; bottom: 12px;
    font-family: "Poppins", sans-serif; font-weight: 600;
    font-size: 11px; color: var(--check-text);
  }

  .animal-photo {
    position: absolute; left: 215px; right: 0; top: 0; bottom: 0;
    background:
      radial-gradient(ellipse at 78% 35%, var(--photo-cream), transparent 55%),
      radial-gradient(ellipse at 35% 45%, var(--photo-warm), transparent 60%),
      linear-gradient(90deg, rgba(255,255,255,0), #cfc6b6 40%, #ddd3bf);
  }
</style>
</head>
<body>
<div class="canvas">
  <section class="label">
    <div class="brand-mark" aria-hidden="true">
      <svg viewBox="0 0 120 120"><circle cx="60" cy="60" r="52" fill="none" stroke="#2a7a4c" stroke-width="4"/></svg>
    </div>
    <h1 class="brand-name">MOSSY'S MEND</h1>

    <div class="tagline-band">Eco-Friendly Pet Care</div>

    <p class="claim-band">None medicated,safe,effective aid<br>providing a healing environment for<br>recovery from fungal and bacterial infections.</p>

    <div class="feature-panel">
      <div class="animal-photo" role="img" aria-label="Photo of a chestnut horse with a halter, a golden retriever and a tabby cat"></div>
      <ul class="feature-list">
        <li><svg class="tick" viewBox="0 0 24 24"><path d="M3 13l6 6L21 4" fill="none" stroke="#7d8b58" stroke-width="2"/></svg>Rain Rot</li>
        <li><svg class="tick" viewBox="0 0 24 24"><path d="M3 13l6 6L21 4" fill="none" stroke="#7d8b58" stroke-width="2"/></svg>Hot Spots</li>
        <li><svg class="tick" viewBox="0 0 24 24"><path d="M3 13l6 6L21 4" fill="none" stroke="#7d8b58" stroke-width="2"/></svg>Surface wounds</li>
        <li><svg class="tick" viewBox="0 0 24 24"><path d="M3 13l6 6L21 4" fill="none" stroke="#7d8b58" stroke-width="2"/></svg>Ringworm</li>
        <li class="more">and MORE!</li>
      </ul>
      <p class="volume">16 fl oz - 473 ml</p>
    </div>
  </section>
</div>
</body>
</html>
```